Lonestar Canopy Services, INC Roof Safety Info Marketing Material

We need a flyer to illustrate roof safety methods we offer with the pictures and descriptions uploaded. We are a Dallas-based commercial roofing company named Lonestar Canopy Services, INC.
We would like to incorporate our dark blues (seen on our website logo). The final design should communicate roof safety and our ability to assess any roof system based on their safety needs.
https://brellwaytops.com/company/about-brellway-tops-inc/

Target Market(s)

Construction industry

Industry/Entity Type

Commercial Roofind

Font styles to use
Serif

```html
<!DOCTYPE html>
<html lang="en">
<head>
<meta charset="utf-8">
<title>Lonestar Canopy Services – Roof Safety Methods</title>
<link rel="stylesheet" href="https://fonts.googleapis.com/css2?family=Exo+2:wght@600;700;800&family=Source+Sans+3:wght@400;600;700&display=swap">
<style>
  :root {
    --royal: #2b3d9c;
    --navy: #1b2668;
    --deep: #141d52;
    --orange: #e8542b;
    --white: #ffffff;
    --page-bg: #e9e9ec;
  }
  * { box-sizing: border-box; margin: 0; padding: 0; }
  html, body { width: 1200px; height: 768px; overflow: hidden; background: var(--page-bg); }
  body { font-family: "Source Sans 3", sans-serif; position: relative; }

  .flyer {
    position: absolute; left: 314px; top: 14px;
    width: 612px; height: 792px;
    transform: scale(0.935); transform-origin: top left;
    background: var(--white); overflow: hidden;
    box-shadow: 0 6px 20px rgba(0,0,0,.25);
  }
  .flyer-shapes { position: absolute; inset: 0; }
  .abs { position: absolute; }

  .brand { left: 36px; top: 70px; display: flex; align-items: center; gap: 8px; }
  .brand-dot { width: 16px; height: 16px; border-radius: 50%; background: var(--royal); }
  .brand-name { font-family: "Exo 2", sans-serif; font-weight: 700; font-size: 13px; color: var(--royal); letter-spacing: .5px; width: 170px; line-height: 1.2; }

  .headline { left: 46px; top: 144px; font-family: "Exo 2", sans-serif; font-weight: 800; color: var(--royal); line-height: 1; }
  .headline .small { display: block; font-size: 26px; }
  .headline .big { display: block; font-size: 37px; margin-top: 2px; }

  .section-title { left: 22px; top: 278px; font-family: "Exo 2", sans-serif; font-weight: 700; font-size: 29px; color: var(--white); }
  .tagline { left: 22px; top: 316px; font-size: 10.5px; font-weight: 700; color: var(--white); }
  .rule { left: 22px; top: 340px; width: 98px; height: 2px; background: var(--orange); }
  .intro { left: 22px; top: 352px; width: 265px; font-size: 9px; line-height: 1.3; color: var(--white); }

  .steps { left: 20px; top: 394px; width: 268px; list-style: none; color: var(--white); font-size: 9px; line-height: 1.3; }
  .steps li { display: flex; gap: 8px; margin-bottom: 12px; }
  .steps .num { font-size: 22px; color: var(--orange); line-height: .9; width: 12px; flex: none; }

  .hazard { left: 305px; width: 292px; display: flex; gap: 8px; color: var(--white); font-size: 8.6px; line-height: 1.2; text-align: justify; }
  .hazard-icon { flex: none; width: 44px; height: 44px; border-radius: 50%; background: var(--royal); border: 2px solid var(--white); display: flex; align-items: center; justify-content: center; }
  .hazard-icon span { width: 20px; height: 20px; border-radius: 4px; background: var(--orange); }

  .photo-ring { width: 136px; height: 136px; border-radius: 50%; background: var(--white); box-shadow: 0 2px 6px rgba(0,0,0,.3); display: flex; align-items: center; justify-content: center; }
  .photo-ring .photo { width: 124px; height: 124px; border-radius: 50%; }
  .p1 { background: linear-gradient(160deg, #d9e6f2, #7d8a95 55%, #e07a3c); }
  .p2 { background: linear-gradient(180deg, #b8d3ee, #e8eef4 55%, #c7ced6); }
  .p3 { background: linear-gradient(150deg, #8fa4b6, #c9d6e0 50%, #d98a46); }

  .caption { top: 654px; width: 188px; font-size: 8.6px; line-height: 1.2; color: var(--navy); font-weight: 600; text-align: justify; }
  .caption-narrow { width: 140px; }

  .cta { left: 18px; top: 744px; font-family: "Exo 2", sans-serif; font-weight: 700; font-size: 10px; color: var(--white); line-height: 1.45; }
  .phone { left: 362px; top: 732px; display: flex; align-items: center; gap: 10px; }
  .phone-badge { width: 32px; height: 32px; border-radius: 50%; background: var(--orange); border: 2px solid var(--white); display: flex; align-items: center; justify-content: center; }
  .phone-number { font-family: "Exo 2", sans-serif; font-weight: 700; font-size: 24px; color: var(--white); white-space: nowrap; }
  .contact { left: 296px; top: 770px; display: flex; gap: 10px; font-family: "Exo 2", sans-serif; font-weight: 700; font-size: 10px; line-height: 1; color: var(--white); white-space: nowrap; }
  .contact span { display: inline-flex; align-items: center; }
  .contact span::before { content: ""; display: inline-block; width: 7px; height: 7px; border: 1.5px solid var(--white); border-radius: 50%; margin-right: 5px; flex: none; }
</style>
</head>
<body>
<div class="flyer">
  <svg class="flyer-shapes" width="612" height="792" viewBox="0 0 612 792" aria-hidden="true">
    <defs>
      <linearGradient id="heroTone" x1="0" y1="0" x2="1" y2="1">
        <stop offset="0" stop-color="#eef3f8"/>
        <stop offset=".45" stop-color="#b9cde0"/>
        <stop offset=".7" stop-color="#e0703a"/>
        <stop offset="1" stop-color="#3c4f7a"/>
      </linearGradient>
    </defs>
    <rect x="200" y="0" width="412" height="300" fill="url(#heroTone)" role="img" aria-label="Photo of a roofer in a hard hat and harness working on a metal roof"/>
    <path d="M200 0 Q 260 140 200 300 L200 0 Z" fill="#ffffff" opacity=".9"/>
    <path d="M0 262 Q 180 215 400 238 Q 540 252 612 232 L612 300 L0 300 Z" fill="#ffffff"/>
    <path d="M0 272 Q 180 228 400 250 Q 540 262 612 246" fill="none" stroke="var(--royal)" stroke-width="3"/>
    <path d="M0 282 Q 180 240 400 262 Q 540 274 612 262 L612 586 L0 586 Z" fill="var(--royal)"/>
    <rect x="0" y="736" width="612" height="56" fill="var(--deep)"/>
    <path d="M290 756 L612 748 L612 792 L276 792 Z" fill="var(--royal)"/>
  </svg>

  <div class="abs brand">
    <span class="brand-dot"></span>
    <span class="brand-name">LONESTAR CANOPY SERVICES, INC</span>
  </div>

  <h1 class="abs headline"><span class="small">ROOF SAFETY</span><span class="big">METHODS</span></h1>

  <h2 class="abs section-title">ROOF SAFETY</h2>
  <p class="abs tagline">At Lonestar Canopy Services, safety is our main priority.</p>
  <div class="abs rule"></div>
  <p class="abs intro">Throughout our inspection, our roofing experts assess your building, identifying three main areas of safety protocol. These areas include:</p>

  <ol class="abs steps">
    <li><span class="num">1.</span><span>Evidence of rooftop anchorage to provide safe access to your roof, fall protection systems to allow employees</span></li>
    <li><span class="num">2.</span><span>Workers to safely operate on your roof</span></li>
    <li><span class="num">3.</span><span>Protection around fall hazards on your rooftop such as skylights, mechanical or ladder areas</span></li>
  </ol>

  <div class="abs hazard" style="top:306px">
    <div class="hazard-icon"><span></span></div>
    <p>Falls are the leading cause of death in the construction industry. Contractors and facility representatives encounter many hazards on the job, including dangers associated with working at great heights with power tools, electricity, noise, and extreme temperatures.</p>
  </div>
  <div class="abs hazard" style="top:372px">
    <div class="hazard-icon"><span></span></div>
    <p>A lack of fall protection, damaged fall protection equipment, or improper setup can drastically increase a roofer's risk of falling. Unless these hazards are mitigated by the property owner or employer, contractors and facility representatives alike are at risk for serious injury or death.</p>
  </div>
  <div class="abs hazard" style="top:452px">
    <div class="hazard-icon"><span></span></div>
    <p>Following our inspection, our team will thoroughly review and recommend a fall prevention plan that is tailored to your specific needs. Our goal is to provide you with a system that is safe, OSHA compliant, and easy to use.</p>
  </div>

  <div class="abs photo-ring" style="left:44px;top:504px"><div class="photo p1" role="img" aria-label="Photo of two roofers in harnesses climbing a roof frame"></div></div>
  <div class="abs photo-ring" style="left:239px;top:504px"><div class="photo p2" role="img" aria-label="Photo of a worker in safety gear on a flat commercial roof"></div></div>
  <div class="abs photo-ring" style="left:434px;top:504px"><div class="photo p3" role="img" aria-label="Photo of a worker beside rooftop skylights"></div></div>

  <p class="abs caption" style="left:20px">The most important thing (fairly new), if there is an accident on a building, the building owner is responsible for that accident. Previously it fell on the property manager.</p>
  <p class="abs caption" style="left:215px">OSHA guidelines outlined it. Anything with mechanical equipment or any work within 15 feet of a building edge over 6 feet off the ground. Either guard rails or roof anchors. It's all dependent on your specific situation which is where we come into play. We can make that assessment.</p>
  <p class="abs caption caption-narrow" style="left:436px">Skylights are a fall-hazard to consider. Roof hatches as well.</p>

  <p class="abs cta">FOR MORE INFORMATION ON HOW WE CAN<br>ENSURE THE SAFETY OF YOUR ROOF, CALL US TODAY!</p>
  <div class="abs phone">
    <div class="phone-badge">
      <svg width="16" height="16" viewBox="0 0 24 24" aria-hidden="true"><path d="M6.6 10.8a15.2 15.2 0 0 0 6.6 6.6l2.2-2.2a1 1 0 0 1 1-.25 11.4 11.4 0 0 0 3.6.57 1 1 0 0 1 1 1V20a1 1 0 0 1-1 1A17 17 0 0 1 3 4a1 1 0 0 1 1-1h3.5a1 1 0 0 1 1 1c0 1.25.2 2.45.57 3.6a1 1 0 0 1-.25 1z" fill="#fff"/></svg>
    </div>
    <span class="phone-number">(972) 555-0148</span>
  </div>
  <div class="abs contact"><span>www.brellwaytops.com</span><span>service@brellwaytops.com</span></div>
</div>
</body>
</html>
```